Social Media Overlay for Ormond Real Estate

We need an social media overlay that can be added to a photo of a house that includes our current logo and a call to action of "Just Listed". This needs to be something that we can use for every new house that we list. Attached is our current logo in both company colors, purple and white. An example of a overlay from Plazeo that we like.

Target Market(s)

Social Media Real Estate Community - Real Estate Agents, Brokers, Buyers & Sellers

Industry/Entity Type

Real Estate

Font styles to use
Sans Serif

Colors
6c459b

Requirements
Must have
• the company colors, purple and white and the company logo
Nice to have
• call to action "Just Listed"
• some layered, texture, or 3-D effect
Should not have
• Should be clean and simple; nothing too busy

```html
<!DOCTYPE html>
<html lang="en">
<head>
<meta charset="utf-8">
<title>Ormond Real Estate – Just Listed Overlay</title>
<link rel="stylesheet" href="https://fonts.googleapis.com/css2?family=Questrial&family=Oswald:wght@600&display=swap">
<style>
  :root {
    --page-bg: #8a8a8a;
    --brand-purple: #6c459b;
    --logo-purple: #5f2a8c;
    --button-top: #8a4fc0;
    --button-bottom: #4d1a7e;
    --white: #ffffff;
    --sky: #a9d3f2;
    --house: #b9a98f;
    --lawn: #6fae3e;
  }
  html, body {
    margin: 0;
    padding: 0;
    width: 1200px;
    height: 1200px;
    overflow: hidden;
    background: var(--page-bg);
  }
  .canvas {
    position: relative;
    width: 1200px;
    height: 1200px;
  }
  .overlay-banner {
    position: absolute;
    left: 120px;
    top: 422px;
    width: 960px;
    height: 355px;
    background: var(--white);
    box-shadow: 0 8px 22px rgba(0,0,0,0.18);
    overflow: hidden;
  }
  .listing-photo {
    position: absolute;
    left: 0;
    top: 0;
    width: 566px;
    height: 355px;
    background: linear-gradient(180deg, var(--sky) 0%, #cfe3ef 22%, var(--house) 38%, #9c8f7c 62%, var(--lawn) 78%, #5d9a33 100%);
  }
  .accent-shapes {
    position: absolute;
    inset: 0;
    width: 960px;
    height: 355px;
  }
  .logo-name,
  .logo-tagline {
    position: absolute;
    left: 581px;
    width: 354px;
    text-align: center;
    white-space: nowrap;
    color: var(--logo-purple);
    font-family: "Questrial", sans-serif;
    font-weight: 400;
    line-height: 1;
  }
  .logo-name {
    top: 62px;
    font-size: 97px;
    letter-spacing: -3px;
  }
  .logo-tagline {
    top: 171px;
    font-size: 63px;
    letter-spacing: -0.5px;
  }
  .logo-rule {
    position: absolute;
    left: 660px;
    top: 235px;
    width: 194px;
    height: 2px;
    background: var(--logo-purple);
  }
  .cta-button {
    position: absolute;
    left: 603px;
    top: 249px;
    width: 316px;
    height: 91px;
    border-radius: 26px;
    background: linear-gradient(180deg, var(--button-top) 0%, #6a30a3 45%, var(--button-bottom) 100%);
    box-shadow: inset 0 2px 3px rgba(255,255,255,0.35), 0 2px 4px rgba(0,0,0,0.25);
    display: flex;
    align-items: center;
    justify-content: center;
    font-family: "Oswald", sans-serif;
    font-weight: 600;
    font-size: 50px;
    letter-spacing: -1px;
    color: #e9e9ee;
  }
  .cta-button span {
    background: linear-gradient(180deg, #ffffff 0%, #d6d6dc 55%, #9e9ea8 100%);
    -webkit-background-clip: text;
    background-clip: text;
    color: transparent;
    filter: drop-shadow(0 2px 1px rgba(0,0,0,0.45));
  }
</style>
</head>
<body>
  <main class="canvas">
    <section class="overlay-banner">
      <div class="listing-photo" role="img" aria-label="Photo of the newly listed house: two-storey home with porch, garage and front lawn under a blue sky"></div>
      <svg class="accent-shapes" viewBox="0 0 960 355" aria-hidden="true">
        <polygon points="0,0 42,42 42,227 145,355 0,355" fill="var(--brand-purple)"/>
        <polygon points="899,0 960,0 960,270 939,245 939,42" fill="var(--brand-purple)"/>
      </svg>
      <div class="logo-name">Ormond</div>
      <div class="logo-tagline">Real Estate</div>
      <div class="logo-rule"></div>
      <div class="cta-button"><span>JUST LISTED</span></div>
    </section>
  </main>
</body>
</html>
```